Music Industry Business Needs a Business Card Design

Copper Lantern is an audio mastering company that has been in business for 20 years. Mastering is the final creative step in the music production chain. Our job is to make the music sound as good as it possibly can prior to release to the public. Our world is technical, artistic, precise. We work on everything from independent artists to the music for the Grandfield Cup. We are looking for a new, more modern business card design. I am uploading a copy of our logo, although it doesn't absolutely need to be included in the design.

Target Market(s)

Music Industry Professionals

Industry/Entity Type

Business

Contact Information for Business Card

Address, Phone, Email, Website, Name, Job Title

Font styles to use
Sans Serif

Requirements
Must have
• Sorry, but I don't have any concrete things to request. If I had a clear idea of what I want, I would probably just design something myself. I am looking for fresh input and thought I would try this.
Should not have
• Anything that is typical, such as headphones or the like.

```html
<!DOCTYPE html>
<html lang="en">
<head>
<meta charset="utf-8">
<title>Copper Lantern – Business Card</title>
<link rel="stylesheet" href="https://fonts.googleapis.com/css2?family=Cinzel:wght@500&family=Source+Sans+3:wght@400;600&display=swap">
<style>
  :root {
    --backdrop: #8b5e3c;
    --metal-dark: #050505;
    --metal-mid: #2b2b2b;
    --metal-light: #4a4a4a;
    --paper: #ffffff;
    --plum: #3f1a52;
    --silver: #a9a9ad;
    --ink: #333333;
    --logo-ink: #111111;
    --name-ink: #ffffff;
  }
  html, body {
    margin: 0;
    width: 1200px;
    height: 720px;
    overflow: hidden;
    background: var(--backdrop);
  }
  .canvas {
    width: 1200px;
    height: 720px;
    display: flex;
    align-items: center;
    justify-content: center;
  }
  .business-card {
    width: 1160px;
    height: 662px;
    display: block;
  }
  .contact-line, .address-line {
    font-family: "Source Sans 3", sans-serif;
    font-size: 17px;
    fill: var(--ink);
  }
  .contact-label, .web-prefix {
    font-weight: 600;
    fill: var(--plum);
  }
  .brand-name {
    font-family: "Source Sans 3", sans-serif;
    font-size: 36px;
    font-weight: 400;
    fill: var(--logo-ink);
  }
  .holder-name {
    font-family: "Cinzel", serif;
    font-size: 25px;
    font-weight: 500;
    fill: var(--name-ink);
    letter-spacing: 0.5px;
  }
</style>
</head>
<body>
<main class="canvas">
  <svg class="business-card" viewBox="0 0 710 405" xmlns="http://www.w3.org/2000/svg" aria-label="Copper Lantern business card">
    <defs>
      <linearGradient id="brushed-metal" x1="0" y1="0" x2="1" y2="0">
        <stop offset="0" stop-color="var(--metal-dark)"/>
        <stop offset="0.35" stop-color="var(--metal-mid)"/>
        <stop offset="0.55" stop-color="var(--metal-light)"/>
        <stop offset="0.75" stop-color="var(--metal-dark)"/>
        <stop offset="1" stop-color="var(--metal-mid)"/>
      </linearGradient>
      <path id="wave-top" d="M0,118 C150,95 300,80 380,50 C450,25 560,30 710,48"/>
      <path id="wave-bottom" d="M0,322 C80,360 200,385 330,362 C450,340 600,290 710,282"/>
    </defs>

    <rect class="card-ground" width="710" height="405" fill="url(#brushed-metal)"/>

    <g class="wave-bands" fill="none">
      <use href="#wave-top" transform="translate(0,-15)" stroke="var(--plum)" stroke-width="10"/>
      <use href="#wave-top" transform="translate(0,-4)" stroke="var(--silver)" stroke-width="9"/>
      <use href="#wave-bottom" transform="translate(0,6)" stroke="var(--plum)" stroke-width="9"/>
      <use href="#wave-bottom" transform="translate(0,15)" stroke="var(--silver)" stroke-width="7"/>
    </g>

    <path class="wave-panel" fill="var(--paper)"
      d="M0,118 C150,95 300,80 380,50 C450,25 560,30 710,48 L710,282 C600,290 450,340 330,362 C200,385 80,360 0,322 Z"/>

    <text class="brand-name" x="84" y="256">COPPER LANTERN</text>

    <g class="contact-block" text-anchor="end">
      <text class="contact-line" x="655" y="116"><tspan class="contact-label">Tel:</tspan> 012.345.6789</text>
      <text class="contact-line" x="655" y="140"><tspan class="contact-label">Email:</tspan> info@copperlantern.ca</text>
      <text class="contact-line" x="655" y="173"><tspan class="web-prefix">www.</tspan>copperlantern<tspan class="web-prefix">.</tspan>ca</text>
      <text class="address-line" x="655" y="219">Suite 000, Cityname</text>
      <text class="address-line" x="655" y="243">country name</text>
    </g>

    <text class="holder-name" x="653" y="358" text-anchor="end">Your name here</text>
  </svg>
</main>
</body>
</html>
```